Harborline Self Storage

looking for a clean sharp easy to read advertising billboard to rent units

online rentals
online payment
online check out

climate control units available
competitive rates

https://www.harborline-selfstorage.example/

```html
<!DOCTYPE html>
<html lang="en">
<head>
<meta charset="utf-8">
<title>Harborline Self Storage – Billboard</title>
<link rel="stylesheet" href="https://fonts.googleapis.com/css2?family=Anton&family=Archivo+Black&display=swap">
<style>
  :root {
    --navy: #1e2a78;
    --navy-deep: #17205e;
    --red: #e8212b;
    --red-bright: #f2333a;
    --white: #ffffff;
    --backdrop: #b9cde0;
  }
  * { margin: 0; padding: 0; box-sizing: border-box; }
  html, body {
    width: 1200px; height: 840px; overflow: hidden;
    background: var(--backdrop);
  }
  .billboard {
    position: absolute; left: 40px; top: 105px;
    width: 1120px; height: 630px;
    background: var(--white);
    overflow: hidden;
    box-shadow: 0 6px 24px rgba(20, 30, 60, 0.25);
  }
  .billboard-shapes { position: absolute; inset: 0; }
  .brand {
    position: absolute; left: 380px; top: 36px;
    display: flex; align-items: center; gap: 18px;
  }
  .brand-mark { width: 24px; height: 24px; background: var(--red); flex: none; }
  .brand-name {
    font-family: "Archivo Black", sans-serif;
    color: var(--navy);
    font-size: 42px; line-height: 1.05; letter-spacing: 1px;
  }
  .headline {
    position: absolute; left: 50px; top: 178px;
    font-family: "Anton", sans-serif;
    font-size: 210px; line-height: 1;
    letter-spacing: 5px;
    white-space: nowrap;
    color: var(--navy);
    background: linear-gradient(180deg, #2b3aa0 0%, var(--navy-deep) 100%);
    -webkit-background-clip: text; background-clip: text;
    -webkit-text-fill-color: transparent;
  }
  .services {
    position: absolute; left: 690px; top: 252px;
    font-family: "Archivo Black", sans-serif;
    color: var(--white);
    font-size: 38px; line-height: 48px;
    white-space: nowrap;
  }
  .services li { list-style: none; }
  .features {
    position: absolute; left: 240px; top: 428px; width: 840px;
    text-align: center;
    font-family: "Archivo Black", sans-serif;
    color: var(--white);
    font-size: 24px; line-height: 40px; letter-spacing: 0.5px;
  }
  .features .star, .contact .star { color: var(--red-bright); }
  .contact {
    position: absolute; left: 0; right: 0; top: 540px;
    display: flex; justify-content: center; align-items: center; gap: 22px;
    font-family: "Anton", sans-serif;
    color: var(--navy);
    font-size: 52px; line-height: 1;
    white-space: nowrap;
  }
  .contact .star { font-family: "Archivo Black", sans-serif; font-size: 28px; }
</style>
</head>
<body>
  <main class="billboard">
    <svg class="billboard-shapes" width="1120" height="630" viewBox="0 0 1120 630" aria-hidden="true">
      <rect x="0" y="390" width="1120" height="30" fill="var(--navy)" />
      <polygon fill="var(--red)" points="0,420 200,420 228,480 0,480" />
      <polygon fill="var(--navy)" points="200,420 1120,420 1120,470 895,470 865,515 245,515" />
      <polygon fill="var(--red)" points="895,470 1120,470 1120,515 865,515" />
      <polygon fill="var(--red)"
        points="640,238 1120,238 1120,408 630,408 646,386 628,362 644,338 630,312 646,286 632,262" />
      <polygon fill="var(--red-bright)" points="640,238 1120,238 1120,310 646,286 632,262" opacity="0.6" />
    </svg>

    <div class="brand">
      <span class="brand-mark"></span>
      <div class="brand-name">HARBORLINE<br>SELF STORAGE</div>
    </div>

    <h1 class="headline">ONLINE</h1>

    <ul class="services">
      <li>RENTALS</li>
      <li>PAYMENT</li>
      <li>CHECK OUT</li>
    </ul>

    <p class="features">
      <span class="star">★</span> CLIMATE CONTROL UNITS AVAILABLE <span class="star">★</span><br>
      <span class="star">★</span> COMPETITIVE RATES <span class="star">★</span>
    </p>

    <p class="contact">
      <span class="phone">555.014.2700</span>
      <span class="star">★</span>
      <span class="web">HARBORLINE-SELFSTORAGE.EXAMPLE</span>
    </p>
  </main>
</body>
</html>
```